"Cork Hollow Excursions" is a top notch Santa Barbara County Wine Tour company.

We provide scenic, boutique and custom wine tours. I need the card to be clean and classy. I will provide our logo. I would like the logo to cover the back side of the card as an option and would like to see a couple color options other then our signature green and gold. I would like to see some creative options and let the designers come up with options.
I need cards for myself and my team. The final design should communicate "An authentic and boutique wine tour experience"
Please use my website for reference www.corkhollowexcursions.com

Target Market(s)

We have a wide range of clients from millennials to baby boomers

Industry/Entity Type

Tour

Contact Information for Business Card

Contact info:
Dale Munford
805-291-6384
info@corkhollowexcursions.com
corkhollowexcursions.com

Colors

Designer to choose colors to be used in the design.

Requirements
Must have
• my logo
Nice to have
• *I would like to have the backside side with the logo and the company statement
• "An authentic and boutique wine tour experience" as an option.
• *I would also like to see what the designers can create!
• *I would like to see an option that incorporates or social: snapgrid, rovia, route scout
Should not have
• I do not want it too busy.

```html
<!DOCTYPE html>
<html lang="en">
<head>
<meta charset="UTF-8">
<title>Cork Hollow Excursions – Business Card</title>
<link href="https://fonts.googleapis.com/css2?family=Arimo:wght@400;700&display=swap" rel="stylesheet">
<style>
  :root {
    --backdrop: #e6e6ea;
    --card: #ffffff;
    --ink: #111111;
    --brand-green: #3f6b3c;
    --rule: #1a1a1a;
    --mark: #9a7b4f;
    --card-shadow: rgba(40, 40, 60, 0.14);
  }
  * { box-sizing: border-box; margin: 0; padding: 0; }
  html, body {
    width: 1200px;
    height: 600px;
    overflow: hidden;
    background: var(--backdrop);
    font-family: "Arimo", Arial, sans-serif;
  }
  .sheet {
    width: 1200px;
    height: 600px;
    display: flex;
    align-items: center;
    justify-content: center;
    gap: 60px;
  }
  .card {
    width: 520px;
    height: 300px;
    background: var(--card);
    box-shadow: 0 6px 18px var(--card-shadow);
    position: relative;
  }
  .card--logo {
    display: flex;
    align-items: center;
    justify-content: center;
  }
  .brand-name {
    color: var(--brand-green);
    font-weight: 700;
    letter-spacing: 0.04em;
    text-transform: uppercase;
    display: flex;
    align-items: center;
    gap: 10px;
  }
  .brand-name__dot {
    width: 12px;
    height: 12px;
    border-radius: 50%;
    background: var(--brand-green);
  }
  .card--logo .brand-name { font-size: 22px; }
  .card--contact .brand-name {
    position: absolute;
    top: 22px;
    left: 40px;
    font-size: 11px;
    gap: 6px;
  }
  .card--contact .brand-name__dot { width: 7px; height: 7px; }
  .contact {
    position: absolute;
    top: 58px;
    left: 40px;
    color: var(--ink);
    font-size: 22px;
    line-height: 1.12;
  }
  .divider {
    position: absolute;
    left: 395px;
    top: 70px;
    width: 2px;
    height: 160px;
    background: var(--rule);
  }
  .social {
    position: absolute;
    left: 418px;
    top: 118px;
    list-style: none;
    display: flex;
    flex-direction: column;
    gap: 10px;
  }
  .social__item {
    display: flex;
    align-items: center;
    gap: 6px;
    font-size: 11px;
    color: var(--ink);
  }
  .social__item::before {
    content: "";
    width: 12px;
    height: 12px;
    background: var(--mark);
  }
</style>
</head>
<body>
  <main class="sheet">
    <section class="card card--logo" aria-label="Card front">
      <div class="brand-name"><span class="brand-name__dot"></span>Cork Hollow Excursions</div>
    </section>

    <section class="card card--contact" aria-label="Card back">
      <div class="brand-name"><span class="brand-name__dot"></span>Cork Hollow Excursions</div>
      <address class="contact" style="font-style: normal;">
        Contact info:<br>
        Dale Munford<br>
        805-291-6384<br>
        info@corkhollowexcursions.com<br>
        corkhollowexcursions.com
      </address>
      <div class="divider"></div>
      <ul class="social">
        <li class="social__item">snapgrid</li>
        <li class="social__item">chatterly</li>
        <li class="social__item">friendwall</li>
      </ul>
    </section>
  </main>
</body>
</html>
```